Bright Path Flyer Design for Virtual Online Clinic. -5.5 x 8.5 inches (half sheet)

We need a clean, modern flyer design for Bright Path, a new virtual walk-in clinic based in British Columbia. The flyer will be used in libraries, pharmacies, and community centers to help residents easily access primary care through their Bright Path NFC access card.
The flyer will ask a question : NEED A DOCTOR? This should be large and attention grabbing.
The design should clearly feature a Bright Path card image (the access card) as the centerpiece and visually show how patients can use it to book appointments. The tone should feel trustworthy, healthcare-oriented, and community-friendly — clean fonts, clear spacing, and strong readability from a distance.

Side One: This card has the NFC Access Card.
NEED A DOCTOR? (Large Font, Attention Grabbing)
How to Book an Appointment using your Bright Path Card
Step 1: Tap Your Card on Your Phone
Hold your card near the back of your phone.
It will activate automatically — no app needed.
The Bright Path scheduler will open.
Step 2: Schedule Your Appointment
Select your clinical concern.
Choose your time window.
Register (only once).
Confirm your appointment.
Step 3: Relax, we’ll take care of the rest
A doctor will call during your scheduled time.
Once booked, you’ll be able to call our office.
No emails, no texts — just a real person.
It’s that simple.
Side Two:
About Bright Path
Created by Dr. Marcus Ferrigan
Bright Path was founded to make healthcare simple and convenient. Prescription renewals. Common infections. Medical notes. And so much more.
Our doctors can address 120+ health concerns virtually — providing quality care without the waiting room. No waiting rooms. Just real doctors providing real care.
Why Patients Choose Bright Path
Easy access – book and be seen from anywhere in BC.
Effortless booking – tap your Bright Path Card to begin.
Trusted physicians – every visit is with a licensed BC family doctor.
How It Works
Book your visit — choose a time window that fits your day.
Join the queue — you’ll be called when it’s your turn.
Speak directly with your doctor — simple, secure, and stress-free.
Convenient Care for Common Concerns

Additional Details.
Please find the domain to be launched soon. I've attached the NFC card file for review, it is 85.5 mm x 54 mm. The card will be glued to the flyer.
I've attached examples of flyers but they are not the look I am seeking and I am looking for creative solutions.
Thank you!
http://brightpath-example.test/

Adult Patients in British Columbia

Healthcare

• Looking for clean lines, uniform appearance, and high legibility i.e poppins

0054AA
0677BA
7BADD7
CADEEF
E8F1F8

• Need A Doctor?
• Elegant style, not too busy, clear layout.
• Clutter, look cheap - review examples.

```html
<!DOCTYPE html>
<html lang="en">
<head>
<meta charset="utf-8">
<title>Bright Path Flyer</title>
<link href="https://fonts.googleapis.com/css2?family=Poppins:wght@300;400;500;600;700;800&display=swap" rel="stylesheet">
<style>
  :root {
    --backdrop: #a9aeb2;
    --navy: #2b4189;
    --ink: #16214f;
    --deep: #0c0f4e;
    --step: #0a5cc0;
    --footer-light: #5070d8;
    --white: #ffffff;
  }
  * { box-sizing: border-box; margin: 0; padding: 0; }
  html, body { width: 1200px; height: 898px; overflow: hidden; }
  body {
    background: var(--backdrop);
    font-family: "Poppins", sans-serif;
    position: relative;
  }
  .flyer {
    position: absolute;
    top: 108px;
    width: 440px;
    height: 681px;
    overflow: hidden;
    background: var(--white);
  }
  .flyer--front { left: 117px; }
  .flyer--back { left: 643px; }

  .brand-name {
    position: absolute;
    left: 0; right: 0;
    text-align: center;
    font-family: "Poppins", sans-serif;
    font-weight: 500;
    font-size: 30px;
    letter-spacing: 0.5px;
  }

  /* Front */
  .front-top .brand-name { top: 56px; color: var(--navy); }
  .headline {
    position: absolute;
    left: 0; right: 0;
    top: 112px;
    text-align: center;
    color: var(--navy);
    font-weight: 800;
    font-size: 76px;
    line-height: 64px;
    letter-spacing: -1px;
  }
  .subhead {
    position: absolute;
    left: 0; right: 0;
    top: 266px;
    text-align: center;
    color: var(--ink);
    font-weight: 600;
    font-size: 17px;
    line-height: 20px;
  }
  .steps-band {
    position: absolute;
    left: 0; top: 334px;
    width: 440px; height: 297px;
    background: var(--navy);
  }
  .step {
    position: absolute;
    left: 74px;
    width: 330px;
  }
  .step-badge {
    position: absolute;
    left: 0; top: 0;
    width: 62px; height: 62px;
    border-radius: 50%;
    border: 2.5px solid var(--white);
    background: var(--step);
    color: var(--white);
    text-align: center;
  }
  .step-badge .label { display: block; font-weight: 500; font-size: 11.5px; line-height: 12px; margin-top: 10px; }
  .step-badge .num { display: block; font-weight: 700; font-size: 26px; line-height: 28px; }
  .step-text {
    position: absolute;
    left: 78px;
    color: var(--white);
    font-weight: 400;
    font-size: 8.6px;
    line-height: 12px;
    white-space: nowrap;
  }
  .step-text .closing { font-size: 9.6px; }
  .step--one { top: 33px; }
  .step--one .step-text { top: 0; }
  .step--two { top: 124px; }
  .step--two .step-text { top: -6px; }
  .step--three { top: 215px; }
  .step--three .step-text { top: -6px; }

  .contact-bar {
    position: absolute;
    left: 0; bottom: 0;
    width: 440px; height: 50px;
    display: flex;
    align-items: center;
    justify-content: center;
    gap: 12px;
    color: var(--white);
    font-weight: 300;
    font-size: 24px;
    letter-spacing: 0.5px;
  }
  .contact-bar svg { width: 30px; height: 30px; }
  .flyer--front .contact-bar { background: var(--footer-light); }
  .flyer--back .contact-bar { background: var(--navy); }

  /* Back */
  .about-band {
    position: absolute;
    left: 0; top: 0;
    width: 440px; height: 328px;
    background: var(--navy);
    color: var(--white);
  }
  .about-title {
    position: absolute;
    left: 0; right: 0; top: 34px;
    text-align: center;
    font-weight: 800;
    font-size: 29px;
    letter-spacing: 0.5px;
  }
  .about-band .brand-name { top: 96px; color: var(--white); }
  .creator-tag {
    position: absolute;
    left: 88px; top: 148px;
    width: 266px; height: 27px;
    background: var(--deep);
    color: var(--white);
    font-weight: 700;
    font-size: 13px;
    line-height: 27px;
    text-align: center;
  }
  .about-copy {
    position: absolute;
    left: 20px; right: 20px;
    text-align: center;
    font-weight: 300;
    font-size: 11px;
    line-height: 14.5px;
  }
  .about-copy--first { top: 190px; }
  .about-copy--second { top: 241px; }

  .why-title {
    position: absolute;
    left: 0; right: 0; top: 362px;
    text-align: center;
    color: var(--navy);
    font-weight: 700;
  }
  .why-title .small { display: block; font-size: 16px; line-height: 20px; }
  .why-title .large { display: block; font-size: 22px; line-height: 26px; }
  .benefits {
    position: absolute;
    left: 38px; top: 430px;
    list-style: none;
    color: var(--ink);
    font-weight: 300;
    font-size: 11.4px;
  }
  .benefits li { position: relative; padding-left: 20px; line-height: 16.5px; margin-bottom: 5.5px; white-space: nowrap; }
  .benefits li svg { position: absolute; left: 0; top: 3px; width: 12px; height: 10px; }
  .benefits strong { color: var(--navy); font-weight: 600; }
  .benefits .note { display: block; }
</style>
</head>
<body>

<section class="flyer flyer--front">
  <div class="front-top">
    <div class="brand-name">Bright Path</div>
    <h1 class="headline">NEED A<br>DOCTOR?</h1>
    <p class="subhead">HOW TO BOOK AN APPOINTMENT<br>USING YOUR BRIGHT PATH CARD</p>
  </div>

  <div class="steps-band">
    <div class="step step--one">
      <div class="step-badge"><span class="label">STEP</span><span class="num">1</span></div>
      <p class="step-text">→Tap Your Card on Your Phone<br>→ Hold your card near the<br>back of your phone. It will activate automatically –<br>no app needed. The Bright Path scheduler will open.</p>
    </div>
    <div class="step step--two">
      <div class="step-badge"><span class="label">STEP</span><span class="num">2</span></div>
      <p class="step-text">→ Schedule Your Appointment<br>→ Select your clinical concern.<br>→ Choose your time window.<br>→ Register (only once).<br>→ Confirm your appointment.</p>
    </div>
    <div class="step step--three">
      <div class="step-badge"><span class="label">STEP</span><span class="num">3</span></div>
      <p class="step-text">Relax, we'll take care of the rest<br>A doctor will call during your scheduled time.<br>Once booked, you'll be able to call our office.<br>No emails, no texts – just a real person.<br><span class="closing">It's that simple.</span></p>
    </div>
  </div>

  <div class="contact-bar">
    <svg viewBox="0 0 32 32" aria-hidden="true">
      <path d="M9 4c1 0 1.6.5 2 1.4l2 4.4c.4.9.2 1.8-.6 2.4l-1.7 1.4c1.2 2.8 3.4 5 6.2 6.3l1.4-1.7c.6-.8 1.5-1 2.4-.6l4.4 2c.9.4 1.4 1 1.4 2l-.3 3c-.2 1.6-1.4 2.9-3 2.9C13 27.5 4.5 19 4.5 8.3c0-1.6 1.3-2.8 2.9-3z" fill="none" stroke="#fff" stroke-width="2.4" stroke-linejoin="round"/>
      <path d="M19 4.5a9 9 0 0 1 8.5 8.5M19 9a4.5 4.5 0 0 1 4 4" fill="none" stroke="#fff" stroke-width="2.2" stroke-linecap="round"/>
    </svg>
    <span>brightpath-example.test</span>
  </div>
</section>

<section class="flyer flyer--back">
  <div class="about-band">
    <h2 class="about-title">ABOUT</h2>
    <div class="brand-name">Bright Path</div>
    <div class="creator-tag">CREATED BY DR. MARCUS FERRIGAN</div>
    <p class="about-copy about-copy--first">Bright Path was founded to make healthcare simple and<br>convenient. Prescription renewals. Common infections. Medical notes.<br>And so much more.</p>
    <p class="about-copy about-copy--second">Our doctors can address 120+ health concerns virtually –<br>providing quality care without the waiting room. No waiting rooms.<br>Just real doctors providing real care.</p>
  </div>

  <h2 class="why-title"><span class="small">WHY PATIENTS CHOOSE</span><span class="large">BRIGHT PATH</span></h2>

  <ul class="benefits">
    <li><svg viewBox="0 0 12 10"><polyline points="1,5 4.5,8.5 11,1.5" fill="none" stroke="#2b4189" stroke-width="2.2"/></svg><strong>Easy access –</strong> book and be seen from anywhere in BC.</li>
    <li><svg viewBox="0 0 12 10"><polyline points="1,5 4.5,8.5 11,1.5" fill="none" stroke="#2b4189" stroke-width="2.2"/></svg><strong>Effortless booking –</strong> tap your Bright Path Card to begin.</li>
    <li><svg viewBox="0 0 12 10"><polyline points="1,5 4.5,8.5 11,1.5" fill="none" stroke="#2b4189" stroke-width="2.2"/></svg><strong>Trusted physicians –</strong> every visit is with a licensed BC family doctor.<span class="note">How It Works</span></li>
    <li><svg viewBox="0 0 12 10"><polyline points="1,5 4.5,8.5 11,1.5" fill="none" stroke="#2b4189" stroke-width="2.2"/></svg><strong>Book your visit –</strong> choose a time window that fits your day.</li>
    <li><svg viewBox="0 0 12 10"><polyline points="1,5 4.5,8.5 11,1.5" fill="none" stroke="#2b4189" stroke-width="2.2"/></svg><strong>Join the queue –</strong> you'll be called when it's your turn.</li>
    <li><svg viewBox="0 0 12 10"><polyline points="1,5 4.5,8.5 11,1.5" fill="none" stroke="#2b4189" stroke-width="2.2"/></svg><strong>Speak directly with your doctor –</strong> simple, secure, and stress-free.<span class="note">Convenient Care for Common Concerns</span></li>
  </ul>

  <div class="contact-bar">
    <svg viewBox="0 0 32 32" aria-hidden="true">
      <path d="M9 4c1 0 1.6.5 2 1.4l2 4.4c.4.9.2 1.8-.6 2.4l-1.7 1.4c1.2 2.8 3.4 5 6.2 6.3l1.4-1.7c.6-.8 1.5-1 2.4-.6l4.4 2c.9.4 1.4 1 1.4 2l-.3 3c-.2 1.6-1.4 2.9-3 2.9C13 27.5 4.5 19 4.5 8.3c0-1.6 1.3-2.8 2.9-3z" fill="none" stroke="#fff" stroke-width="2.4" stroke-linejoin="round"/>
      <path d="M19 4.5a9 9 0 0 1 8.5 8.5M19 9a4.5 4.5 0 0 1 4 4" fill="none" stroke="#fff" stroke-width="2.2" stroke-linecap="round"/>
    </svg>
    <span>brightpath-example.test</span>
  </div>
</section>

</body>
</html>
```